Envelope design

We need a envelope design for a professional services firm called Brindlemoor Tax Advisory Inc. The firm is essentially a very specialized tax accounting firm - instead of serving the end consumer, we support other public accounting firms in the area of Canadian and U.S. tax advisory and compliance (i.e. they call us on tax issues too complex for the general practitioner). Our byline is "Tax Support Services for Public Accounting Firms". Our postcard should utilize our logo and be based on colours present in our logo (see file attached). The final design needs to convey professionalism and trustworthiness (we're hired by accountants after all!) while being creative and eye-catching. Eye-catching is critical, since many prospective recipients will not have heard from me before and I want them to read the postcard.
At lot of design work has already been done here. I've attached a number of sample files showing logo and letterhead designs. Please note that the letterhead hasn't yet been updated for the new logo. This is happening in a separate design competition.
Updates
Project Deadline Extended Reason: Deadline is extended because I am pricing the extra cost of having colour right to the edge of the envelopes. This will help me design on final design. Pricing should come in on Monday. Added Saturday, February 20, 2016

```html
<!DOCTYPE html>
<html lang="en">
<head>
<meta charset="utf-8">
<title>Brindlemoor Tax Advisory – Stationery</title>
<link rel="stylesheet" href="https://fonts.googleapis.com/css2?family=Cinzel:wght@500&family=Open+Sans:wght@400;600&display=swap">
<style>
  :root{
    --navy:#1b3160;
    --navy-deep:#152a55;
    --blue:#2f63b8;
    --orange:#f0792a;
    --red:#e8452c;
    --gold:#f7b51a;
    --paper:#ffffff;
    --ink:#2a2a2a;
    --muted:#7a7a7a;
    --window:#9a9a9a;
    --fold:#c9c9c9;
    --bg-light:#f4f4f4;
    --bg-dark:#cfcfcf;
  }
  *{box-sizing:border-box;margin:0;padding:0}
  html,body{width:1056px;height:1200px;overflow:hidden}
  body{
    position:relative;
    background:radial-gradient(ellipse at 50% 30%,var(--bg-light) 0%,var(--bg-dark) 100%);
    font-family:"Open Sans",Arial,sans-serif;
  }
  .piece{position:absolute;background:var(--paper);box-shadow:0 4px 10px rgba(0,0,0,.25);overflow:hidden}

  .brand{display:flex;align-items:center;gap:10px}
  .brand-mark{width:20px;height:20px;background:var(--navy);flex:none}
  .brand-name{font-family:"Cinzel",Georgia,serif;font-weight:500;letter-spacing:.02em;line-height:1;white-space:nowrap}
  .brand-tagline{font-family:"Cinzel",Georgia,serif;font-weight:500;text-transform:uppercase;letter-spacing:.16em;color:var(--muted);white-space:nowrap;border-top:1px solid var(--muted);padding-top:3px;margin-top:3px}

  /* decorative swoosh areas, flat soft gradient */
  .swoosh-area{position:absolute}

  /* business card front */
  .card-front{left:86px;top:34px;width:341px;height:194px}
  .card-front .panel{position:absolute;left:0;top:0;width:100%;height:156px;background:var(--navy)}
  .card-front .swoosh-area{right:0;top:0;width:100px;height:156px;
    background:linear-gradient(160deg,var(--blue) 0%,var(--navy) 55%,rgba(240,121,42,.55) 100%)}
  .card-front .brand{position:absolute;left:28px;top:66px;gap:6px}
  .card-front .brand-mark{width:16px;height:16px;background:var(--paper)}
  .card-front .brand-name{font-size:13px;color:var(--paper)}
  .card-front .brand-tagline{font-size:5.5px;color:#d6dbe6;border-color:#d6dbe6}
  .card-front .web{position:absolute;left:0;bottom:12px;width:100%;text-align:center;font-size:11px;font-weight:600;color:var(--red)}

  /* business card back */
  .card-back{left:462px;top:34px;width:341px;height:194px}
  .card-back .brand{position:absolute;left:38px;top:34px;gap:6px}
  .card-back .brand-mark{width:16px;height:16px}
  .card-back .brand-name{font-size:14px;color:var(--ink)}
  .card-back .brand-tagline{font-size:5.5px}
  .card-back .stripe{position:absolute;left:0;top:102px;width:100%;height:5px;background:linear-gradient(90deg,var(--red),var(--orange) 60%,var(--gold))}
  .card-back .panel{position:absolute;left:0;top:107px;width:100%;height:87px;background:var(--navy)}
  .card-back .swoosh-area{left:190px;top:152px;width:120px;height:42px;
    background:linear-gradient(20deg,rgba(240,121,42,.6) 0%,rgba(47,99,184,.45) 60%,var(--navy) 100%)}
  .contact{position:absolute;left:20px;top:127px;list-style:none;font-size:8px;line-height:11.5px;color:var(--paper)}
  .contact b{display:inline-block;width:12px;color:var(--gold);font-weight:600}
  .person{position:absolute;left:200px;top:124px;font-size:17px;font-weight:600;color:var(--gold)}

  /* envelope front */
  .envelope-front{left:86px;top:272px;width:921px;height:435px}
  .envelope-front .brand{position:absolute;left:40px;top:64px}
  .envelope-front .brand-mark{width:30px;height:30px}
  .envelope-front .brand-name{font-size:29px;color:var(--ink)}
  .envelope-front .brand-tagline{font-size:12px;letter-spacing:.2em}
  .envelope-front .stripe{position:absolute;left:0;top:365px;width:100%;height:8px;background:linear-gradient(90deg,var(--red),var(--orange) 60%,var(--gold))}
  .envelope-front .panel{position:absolute;left:0;top:373px;width:100%;height:62px;background:var(--navy)}
  .envelope-front .swoosh-area{right:0;top:373px;width:84px;height:62px;
    background:linear-gradient(135deg,var(--navy-deep) 0%,var(--blue) 55%,rgba(240,121,42,.7) 100%)}
  .envelope-front .window{position:absolute;left:42px;top:283px;width:437px;height:110px;background:var(--window);border-radius:10px}
  .envelope-front .web{position:absolute;right:103px;top:403px;font-size:15px;font-weight:600;color:var(--gold)}

  /* envelope back */
  .envelope-back{left:86px;top:736px;width:921px;height:434px}
  .envelope-back svg{position:absolute;left:0;top:0}
</style>
</head>
<body>

<section class="piece card-front" aria-label="Business card front">
  <div class="panel"></div>
  <div class="swoosh-area" role="img" aria-label="Decorative blue and orange swoosh graphic"></div>
  <div class="brand">
    <span class="brand-mark"></span>
    <div>
      <div class="brand-name">BRINDLEMOOR TAX ADVISORY</div>
      <div class="brand-tagline">Tax support for public accounting firms</div>
    </div>
  </div>
  <p class="web">www.brindlemoortax.example</p>
</section>

<section class="piece card-back" aria-label="Business card back">
  <div class="brand">
    <span class="brand-mark"></span>
    <div>
      <div class="brand-name">BRINDLEMOOR TAX ADVISORY</div>
      <div class="brand-tagline">Tax support for public accounting firms</div>
    </div>
  </div>
  <div class="stripe"></div>
  <div class="panel"></div>
  <div class="swoosh-area" role="img" aria-label="Decorative blue and orange swoosh graphic"></div>
  <ul class="contact">
    <li><b>P</b>: 555.210.4830</li>
    <li><b>F</b>: 555.210.4831</li>
    <li><b>E</b>: avery@brindlemoortax.example</li>
    <li><b>W</b>: www.brindlemoortax.example</li>
  </ul>
  <p class="person">Avery Holt</p>
</section>

<section class="piece envelope-front" aria-label="Envelope front">
  <div class="brand">
    <span class="brand-mark"></span>
    <div>
      <div class="brand-name">BRINDLEMOOR TAX ADVISORY</div>
      <div class="brand-tagline">Tax support for public accounting firms</div>
    </div>
  </div>
  <div class="stripe"></div>
  <div class="panel"></div>
  <div class="swoosh-area" role="img" aria-label="Decorative blue and orange swoosh graphic"></div>
  <div class="window"></div>
  <p class="web">www.brindlemoortax.example</p>
</section>

<section class="piece envelope-back" aria-label="Envelope back">
  <svg width="921" height="434" viewBox="0 0 921 434" aria-hidden="true">
    <path d="M231 150 L19 392 L0 434 M691 150 L900 392 L921 434" fill="none" stroke="var(--fold)" stroke-width="1.5"/>
    <path d="M0 0 H921 C908 40 896 92 862 104 L460 182 L56 104 C24 92 12 40 0 0 Z" fill="var(--navy)"/>
  </svg>
</section>

</body>
</html>
```